PREMIUM AGENCY High End Business Card - A+++ Designers Wanted

** DO NOT ATTEMPT TO CONTACT ME THROUGH SEARCHING ON GOOGLE OR EMAILING ME THROUGH MY WEBSITE **

I need a fresh, contemporary business card designed using the logo attached (VOLKRANE)

I have attached the font for VOLKRANE

It must have a premium look and feel. The business card size must be STANDARD size.

You can submit either/both VERTICAL or HORIZONTAL designs.

FRONT: It must have the following sample information on

Peter Dowle
Director Operations
Mobile +61 452 000 000
Email peterdowle@volkrane.example
www.volkrane.example

The REAR of the business card must have the words

CREATE INSPIRE TOMORROW

as part of the design, in the same font (NEXA) attached.

The words do not need to be in capitals, or on the same line, please design this as you see it best working.

ADDITIONAL INFORMATION
======================

The VOLKRANE logo must be on the front of the card

I want Ultraviolet printing on the final design, to enhance either the NAME of the person OR the VOLKRANE logo OR the words on the back of the card.

Target Market(s)

Agency, Advertising Agency, Creative, Designers

Industry/Entity Type

Media

Contact Information for Business Card

Design Agency, Contemporary, Premium look and feel, High Quality

Font styles to use
Serif
Sans Serif
Other font styles liked:
• ATTACHED TO PROJECT

Requirements
Must have
• BLACK & WHITE as the primary design, and if you feel there can be a highlighted colour, then this can be used.
• The Logo ICON attached is blue, this colour must not be changed.
• I have attached the partner brand VOLKRANE MEDIA incase you need to manipulate the original files.
• ** DO NOT ATTEMPT TO CONTACT ME THROUGH SEARCHING ON GOOGLE OR EMAILING ME THROUGH MY WEBSITE **
Nice to have
• Must be Premium. I have attached some sample designs, that I like that would be a good inspiration for where this can be taken.
• My favourite design is is the SNAPFRAME2-BUSINESSCARD-TEMPLATE
Should not have
• No funny or silly standard / off the shelf designs

```html
<!DOCTYPE html>
<html lang="en">
<head>
<meta charset="UTF-8">
<title>VOLKRANE Business Card</title>
<link rel="stylesheet" href="https://fonts.googleapis.com/css2?family=Montserrat:wght@500;600&family=Lato:wght@400&display=swap">
<style>
  :root {
    --stage: #4b4b4d;
    --card: #2a2a2b;
    --ink: #ffffff;
    --ink-soft: #e6e6e6;
    --accent: #1e9be0;
    --rule: #d8d8d8;
  }
  * { margin: 0; padding: 0; box-sizing: border-box; }
  html, body {
    width: 1200px; height: 900px; overflow: hidden;
    background: var(--stage);
  }
  .canvas {
    position: relative; width: 1200px; height: 900px;
  }
  .card {
    position: absolute; left: 302px;
    width: 596px; height: 340px;
    background: var(--card);
    box-shadow: 0 10px 30px rgba(0,0,0,0.35);
    overflow: hidden;
  }
  .card::after {
    content: ""; position: absolute; left: 0; right: 0; bottom: 0;
    height: 9px; background: var(--accent);
  }
  .card--back { top: 90px; }
  .card--front { top: 470px; }

  /* Back */
  .motto {
    position: absolute; left: 210px; top: 88px;
    font-family: "Montserrat", sans-serif; font-weight: 500;
    font-size: 40px; line-height: 50px; letter-spacing: 3px;
    color: var(--ink); text-transform: uppercase;
  }
  .motto__line:nth-child(2) { padding-left: 8px; }
  .motto__line:nth-child(3) { margin-left: -36px; }
  .motto__initial { color: var(--accent); }

  /* Front */
  .brand {
    position: absolute; left: 42px; top: 44px;
    display: flex; align-items: center; gap: 16px;
  }
  .brand__dot {
    width: 26px; height: 26px; border-radius: 50%;
    background: var(--accent);
  }
  .brand__name {
    font-family: "Montserrat", sans-serif; font-weight: 600;
    font-size: 36px; letter-spacing: 7px; color: var(--ink);
  }
  .person {
    position: absolute; right: 44px; top: 118px; text-align: right;
    font-family: "Lato", sans-serif;
  }
  .person__name { font-size: 27px; color: var(--accent); line-height: 32px; }
  .person__role { font-size: 18px; color: var(--ink-soft); line-height: 24px; }
  .divider {
    position: absolute; left: 42px; right: 44px; top: 184px;
    height: 1px; background: var(--rule);
  }
  .contacts {
    position: absolute; left: 42px; top: 204px;
    font-family: "Lato", sans-serif; font-size: 17px; color: var(--ink-soft);
    list-style: none;
  }
  .contacts li { display: flex; align-items: center; gap: 10px; line-height: 27px; }
  .contacts svg, .phone svg { flex: none; }
  .phone {
    position: absolute; right: 44px; top: 270px;
    display: flex; align-items: center; gap: 12px;
    font-family: "Lato", sans-serif; font-size: 21px; color: var(--ink-soft);
  }
</style>
</head>
<body>
<main class="canvas">
  <section class="card card--back" aria-label="Card back">
    <div class="motto">
      <div class="motto__line"><span class="motto__initial">C</span>reate</div>
      <div class="motto__line"><span class="motto__initial">I</span>nspire</div>
      <div class="motto__line"><span class="motto__initial">T</span>omorrow</div>
    </div>
  </section>

  <section class="card card--front" aria-label="Card front">
    <div class="brand">
      <span class="brand__dot"></span>
      <span class="brand__name">VOLKRANE</span>
    </div>

    <div class="person">
      <div class="person__name">Peter Dowle</div>
      <div class="person__role">Director Operations</div>
    </div>

    <div class="divider"></div>

    <ul class="contacts">
      <li>
        <svg width="16" height="12" viewBox="0 0 16 12" aria-hidden="true">
          <rect x="0.5" y="0.5" width="15" height="11" fill="var(--accent)"/>
          <path d="M0.5 0.5 L8 7 L15.5 0.5" fill="none" stroke="var(--card)" stroke-width="1.2"/>
        </svg>
        peterdowle@volkrane.example
      </li>
      <li>
        <svg width="16" height="16" viewBox="0 0 16 16" aria-hidden="true">
          <circle cx="8" cy="8" r="7.5" fill="var(--accent)"/>
          <g fill="none" stroke="var(--card)" stroke-width="0.9">
            <ellipse cx="8" cy="8" rx="3.2" ry="7.2"/>
            <line x1="0.5" y1="8" x2="15.5" y2="8"/>
            <line x1="2" y1="4.5" x2="14" y2="4.5"/>
            <line x1="2" y1="11.5" x2="14" y2="11.5"/>
          </g>
        </svg>
        www.volkrane.example
      </li>
    </ul>

    <div class="phone">
      <svg width="14" height="22" viewBox="0 0 14 22" aria-hidden="true">
        <rect x="1" y="1" width="12" height="20" rx="2" fill="none" stroke="var(--accent)" stroke-width="1.6"/>
        <rect x="3.5" y="4" width="7" height="7" fill="var(--accent)"/>
        <circle cx="7" cy="17" r="1.3" fill="var(--accent)"/>
      </svg>
      +61 452 000 000
    </div>
  </section>
</main>
</body>
</html>
```